Quietly Meadows needs a brochure

I need to put together a booklet type brochure visually describing what I do. I would like the brochure to have the same elegance as the logo and the business card. I envision using the green design from the back of the business card, on the back of the brochure as well. I would like to have a space for an "About Us" area in which I can explain about the evolution of Quietly Meadows. I would also like to have pictures of work that I have completed. I will send you both copy and photos. I would like the brochure to print matte and be an unusual shape - like a square booklet instead of the normal 8.5x11. I would also like to include the logos of the organizations that I am a member of - NPVO, VORCUS, KREB.
Having some trouble uploading with internet explorer. Will fix the problem and upload ASAP. Thank you all for your patience.

```html
<!DOCTYPE html>
<html lang="en">
<head>
<meta charset="utf-8">
<title>Quietly Meadows – Brochure Cover</title>
<link href="https://fonts.googleapis.com/css2?family=Lato:wght@400;700&display=swap" rel="stylesheet">
<style>
  :root {
    --leaf-green: #a4cd39;
    --leaf-green-soft: #c4df7d;
    --bark-brown: #7a4a2e;
    --paper-white: #ffffff;
    --mist-grey: #eeeeee;
    --bloom-pink: #d9437a;
    --bloom-purple: #8e4fb5;
    --bloom-orange: #f39a1e;
    --bloom-red: #c9202a;
  }
  html, body {
    margin: 0;
    padding: 0;
    width: 1200px;
    height: 600px;
    overflow: hidden;
    background: var(--paper-white);
  }
  .spread {
    position: relative;
    width: 1200px;
    height: 600px;
    display: flex;
    font-family: "Lato", Arial, sans-serif;
  }
  .back-cover {
    position: relative;
    width: 600px;
    height: 600px;
    background: var(--leaf-green);
    overflow: hidden;
  }
  .back-cover__mark {
    position: absolute;
    left: 95px;
    top: 40px;
    width: 400px;
    height: 400px;
  }
  .back-cover__contact {
    position: absolute;
    left: 0;
    right: 0;
    top: 506px;
    text-align: center;
    color: var(--paper-white);
    font-weight: 700;
    font-size: 20px;
    line-height: 27px;
  }
  .front-cover {
    position: relative;
    width: 600px;
    height: 600px;
    overflow: hidden;
    background: linear-gradient(180deg, var(--paper-white) 70%, var(--mist-grey) 100%);
  }
  .front-cover__photo {
    position: absolute;
    left: 0;
    top: 0;
    width: 600px;
    height: 380px;
    background:
      radial-gradient(circle at 20% 25%, var(--bloom-pink) 0, transparent 22%),
      radial-gradient(circle at 60% 30%, var(--bloom-orange) 0, transparent 20%),
      radial-gradient(circle at 85% 15%, var(--bloom-red) 0, transparent 18%),
      radial-gradient(circle at 45% 65%, var(--bloom-red) 0, transparent 18%),
      radial-gradient(circle at 10% 70%, var(--bloom-orange) 0, transparent 18%),
      radial-gradient(circle at 80% 60%, #f2f0ea 0, transparent 16%),
      linear-gradient(135deg, var(--bloom-purple), #b85aa8 50%, var(--bloom-purple));
  }
  .front-cover__wave {
    position: absolute;
    left: 0;
    top: 300px;
    width: 600px;
    height: 120px;
  }
  .tagline {
    position: absolute;
    left: 21px;
    top: 462px;
    margin: 0;
    color: var(--bark-brown);
    font-weight: 400;
    font-size: 36px;
    line-height: 38px;
    letter-spacing: 0.2px;
  }
  .tagline__accent {
    color: var(--leaf-green);
    font-weight: 700;
  }
  .brand-name {
    position: absolute;
    right: 24px;
    top: 488px;
    display: flex;
    align-items: center;
    gap: 10px;
    color: var(--bark-brown);
    font-weight: 400;
    font-size: 26px;
  }
  .brand-name__dot {
    width: 22px;
    height: 22px;
    border-radius: 50%;
    background: var(--leaf-green);
  }
</style>
</head>
<body>
  <main class="spread">
    <section class="back-cover">
      <svg class="back-cover__mark" viewBox="0 0 400 400" aria-hidden="true">
        <circle cx="200" cy="200" r="170" fill="none" stroke="var(--leaf-green-soft)" stroke-width="14"/>
        <text x="200" y="212" text-anchor="middle" font-family="Lato, Arial, sans-serif" font-size="38" font-weight="400" fill="var(--leaf-green-soft)">Quietly Meadows</text>
      </svg>
      <div class="back-cover__contact">
        <div class="contact-phone">Phone: 555-014-2286</div>
        <div class="contact-email">Email: hello@quietlymeadows.example</div>
      </div>
    </section>

    <section class="front-cover">
      <div class="front-cover__photo" role="img" aria-label="Close-up photograph of a colourful bouquet of roses, anthuriums, gerberas and chrysanthemums"></div>
      <svg class="front-cover__wave" viewBox="0 0 600 120" preserveAspectRatio="none" aria-hidden="true">
        <path d="M0 40 C150 -5 330 80 600 20 L600 120 L0 120 Z" fill="var(--leaf-green)"/>
        <path d="M0 48 C150 5 330 88 600 30 L600 120 L0 120 Z" fill="var(--bark-brown)"/>
        <path d="M0 53 C150 12 330 92 600 36 L600 120 L0 120 Z" fill="var(--leaf-green)"/>
        <path d="M0 72 C150 35 330 100 600 52 L600 120 L0 120 Z" fill="var(--paper-white)"/>
      </svg>
      <h1 class="tagline">FILL YOUR LIFE<br>WITH <span class="tagline__accent">COLOR</span></h1>
      <div class="brand-name"><span class="brand-name__dot"></span>Quietly Meadows</div>
    </section>
  </main>
</body>
</html>
```